Handout for attendees of educational seminar

I provide educational workshops on how to give technical presentations at conferences to scientists and engineers. My company is called Craft Talk Studio (www.CraftTalkStudio.example). I would like a double sided, half page size flyer that can be used as a handout for attendees of my workshops. On one side of the flyer, they will get top tips for creating their next presentation. On the other side, they will get my photo, bio, and contact information. I have uploaded a draft of a full page design I made myself. I'd like the copy of the tips to remain the same, but everything else is flexible.

Target Market(s)

scientists, engineers, technical professionals

Font styles to use
Serif
Sans Serif

Requirements
Must have
• my photo (I've provided two options to choose from depending on colors...photo on side 2 only), my logo, flyer needs to be half page in size (5.5" x 8.5"), needs to be double sided, One side has the "tips" and the other side has my personal details (see attached page for copy).
Nice to have
• I like the use of icons on the "tips" side of the flyer.

```html
<!DOCTYPE html>
<html lang="en">
<head>
<meta charset="utf-8">
<title>Craft Talk Studio – Workshop Handout</title>
<link rel="stylesheet" href="https://fonts.googleapis.com/css2?family=Questrial&family=Nunito+Sans:wght@400;700&display=swap">
<style>
:root{
  --green:#2e9e3a;
  --blue:#1b8fdc;
  --blue-dark:#1477bf;
  --ink:#1d1d1f;
  --paper:#ffffff;
  --stage-a:#3b1c6e;
  --stage-b:#c0283a;
  --backdrop:#e9e6e1;
}
*{box-sizing:border-box;margin:0;padding:0}
html,body{width:1200px;height:937px;overflow:hidden;background:var(--backdrop)}
body{position:relative;font-family:'Questrial',sans-serif;color:var(--ink)}
.flyer{position:absolute;top:48px;width:544px;height:840px;background:var(--paper);overflow:hidden;box-shadow:0 6px 22px rgba(0,0,0,.18)}
.flyer--tips{left:37px}
.flyer--bio{left:618px}
.flyer__art{position:absolute;inset:0}
.inset-photo{position:absolute;left:205px;top:165px;width:170px;height:170px;border-radius:50%;border:6px solid var(--blue);background:radial-gradient(circle at 50% 45%,#d9b48a,#8a6a4c 70%,#3a2e26)}
.brand{position:absolute;right:30px;top:34px;display:flex;align-items:center;gap:8px;font-size:17px;color:var(--green)}
.brand__dot{width:30px;height:30px;border-radius:50%;background:#4a4a4a}
.tips__head{position:absolute;left:34px;top:388px;width:480px}
.title{font-size:44px;color:var(--green);line-height:1.05;letter-spacing:.5px}
.kicker{font-size:23px;color:var(--blue);margin-top:4px;letter-spacing:1px}
.tagline{font-family:'Nunito Sans',sans-serif;font-weight:700;font-size:16px;margin-top:2px}
.tips__list{position:absolute;left:30px;right:24px;top:496px;display:flex;flex-direction:column;gap:12px}
.tip{display:flex;gap:24px;align-items:flex-start}
.tip-icon{flex:0 0 56px;display:flex;justify-content:center;padding-top:4px}
.tip__text{flex:1}
.tip__title{font-size:18px;color:var(--green);margin-bottom:2px;line-height:1.2}
.tip__body{font-family:'Nunito Sans',sans-serif;font-size:11px;line-height:1.4}
.band{position:absolute;left:0;right:0;bottom:0;background:var(--blue);color:#fff;display:flex;align-items:center;padding:0 28px}
.band--tips{height:78px}
.band--bio{height:96px}
.contact{display:flex;flex-direction:column;gap:8px;font-size:15px;flex:1}
.contact__row{display:flex;align-items:center;gap:10px}
.band__rule{width:1px;align-self:stretch;margin:14px 18px;background:rgba(255,255,255,.7)}
.follow{font-size:19px}
.follow__icons{display:flex;gap:10px;margin-top:6px}
.follow__icons span{width:20px;height:20px;border-radius:50%;background:var(--blue-dark);border:2px solid #fff}
.bio-block{position:absolute;left:24px;right:40px;top:342px;display:flex;gap:10px}
.quote-mark{font-family:Georgia,serif;font-size:40px;color:var(--green);line-height:.8}
.bio-col{flex:1;display:flex;flex-direction:column}
.bio{font-family:'Nunito Sans',sans-serif;font-size:12px;line-height:1.55}
.bio .quote-mark--close{font-size:26px;line-height:0;vertical-align:-10px;margin-left:4px}
.meet{text-align:right;margin-top:14px}
.meet__name{font-size:24px;color:var(--green);border-bottom:2px solid var(--green);display:inline-block;padding-bottom:2px}
.meet__tag{font-family:'Nunito Sans',sans-serif;font-weight:700;font-size:13px;margin-top:6px}
</style>
</head>
<body>

<section class="flyer flyer--tips">
  <svg class="flyer__art" width="544" height="840" viewBox="0 0 544 840">
    <defs>
      <linearGradient id="stage" x1="0" y1="0" x2="1" y2="1">
        <stop offset="0" stop-color="var(--stage-a)"/>
        <stop offset="1" stop-color="var(--stage-b)"/>
      </linearGradient>
    </defs>
    <rect width="544" height="420" fill="url(#stage)" role="img" aria-label="Photo of the speaker presenting on a conference stage"/>
    <path d="M0,420 L0,385 C140,330 330,250 544,120 L544,840 L0,840Z" fill="var(--paper)"/>
    <path d="M0,372 C140,318 330,238 544,108" fill="none" stroke="var(--green)" stroke-width="10"/>
    <path d="M0,386 C140,332 330,252 544,122" fill="none" stroke="var(--blue)" stroke-width="7"/>
    <path d="M250,0 C250,70 330,112 420,110 C480,108 520,96 544,80 L544,0Z" fill="var(--paper)"/>
    <path d="M250,0 C250,70 330,112 420,110 C480,108 520,96 544,80" fill="none" stroke="var(--blue)" stroke-width="5"/>
  </svg>
  <div class="inset-photo" role="img" aria-label="Portrait photo of the presenter"></div>
  <div class="brand"><span class="brand__dot"></span>Craft Talk Studio</div>

  <header class="tips__head">
    <h1 class="title">Craft Talk Studio</h1>
    <p class="kicker">QUICK TIPS</p>
    <p class="tagline">Science not communicated is science not done!</p>
  </header>

  <div class="tips__list">
    <article class="tip">
      <div class="tip-icon">
        <svg width="48" height="44" viewBox="0 0 52 48"><path d="M4,6 H48 L32,24 V40 L20,46 V24Z" fill="var(--green)"/></svg>
      </div>
      <div class="tip__text">
        <h2 class="tip__title">Be Audience Centered</h2>
        <p class="tip__body">Your ability to be successful as a speaker depends upon your ability to make your audience successful. TIP: Return to “Points of Common Ground” throughout the talk that answer the question “So what?” about the scientific info. Be an interpreter!</p>
      </div>
    </article>

    <article class="tip">
      <div class="tip-icon">
        <svg width="52" height="44" viewBox="0 0 56 48" fill="none" stroke="var(--blue)" stroke-width="3.5" stroke-linecap="round" stroke-linejoin="round">
          <path d="M10,4 V20 M4,14 L10,20 L16,14"/><path d="M28,4 V20 M22,14 L28,20 L34,14"/><path d="M46,4 V20 M40,14 L46,20 L52,14"/>
          <path d="M4,26 H52"/>
          <path d="M18,30 V44 M12,38 L18,44 L24,38"/><path d="M38,30 V44 M32,38 L38,44 L44,38"/>
        </svg>
      </div>
      <div class="tip__text">
        <h2 class="tip__title">Filter &amp; Focus</h2>
        <p class="tip__body">When you try to share everything, you share nothing. TIP: Start your planning with the “view” you want your audience to have at the end of the talk. Then ask yourself “What would they need to know in order to get there?”</p>
      </div>
    </article>

    <article class="tip">
      <div class="tip-icon">
        <svg width="52" height="52" viewBox="0 0 56 56">
          <circle cx="28" cy="28" r="27" fill="#2b2b2b"/>
          <path d="M8,28 C16,16 40,16 48,28 C40,40 16,40 8,28Z" fill="#fff"/>
          <circle cx="28" cy="28" r="8" fill="var(--blue)"/>
          <circle cx="28" cy="28" r="3.5" fill="#2b2b2b"/>
        </svg>
      </div>
      <div class="tip__text">
        <h2 class="tip__title">Show Your Science</h2>
        <p class="tip__body">Your slides should do something for you that your words cannot. This means make your slides VISUAL not VERBAL. TIP: NO BULLET POINTS (seriously!). Have a brief take-away messages supported by visual evidence.</p>
      </div>
    </article>
  </div>

  <footer class="band band--tips">
    <div class="contact">
      <div class="contact__row">
        <svg width="18" height="18" viewBox="0 0 18 18" fill="none" stroke="#fff" stroke-width="1.5"><circle cx="9" cy="9" r="7.5"/><ellipse cx="9" cy="9" rx="3.5" ry="7.5"/><path d="M1.5,9 H16.5"/></svg>
        www.CraftTalkStudio.example
      </div>
      <div class="contact__row">
        <svg width="18" height="18" viewBox="0 0 18 18" fill="none" stroke="#fff" stroke-width="1.5"><rect x="1.5" y="4" width="15" height="10" rx="1"/><path d="M1.5,4 L9,10 L16.5,4"/></svg>
        dana@crafttalkstudio.example
      </div>
    </div>
    <div class="band__rule"></div>
    <div>
      <p class="follow">Follow Us:</p>
      <div class="follow__icons"><span></span><span></span><span></span></div>
    </div>
  </footer>
</section>

<section class="flyer flyer--bio">
  <svg class="flyer__art" width="544" height="840" viewBox="0 0 544 840">
    <defs>
      <linearGradient id="portrait" x1="0" y1="0" x2="1" y2="1">
        <stop offset="0" stop-color="#cfc6b4"/>
        <stop offset=".55" stop-color="#b48a68"/>
        <stop offset="1" stop-color="#2f8a4c"/>
      </linearGradient>
    </defs>
    <rect width="544" height="330" fill="url(#portrait)" role="img" aria-label="Portrait photo of Dana Whitfield"/>
    <path d="M0,290 C160,330 380,300 544,170 L544,840 L0,840Z" fill="var(--paper)"/>
    <path d="M0,290 C160,330 380,300 544,170" fill="none" stroke="var(--blue)" stroke-width="6"/>
  </svg>

  <div class="bio-block">
    <span class="quote-mark">“</span>
    <div class="bio-col">
      <p class="bio">Dana Whitfield is on a mission: to transform how scientists, engineers, and technical professionals present their work. That’s because she believes that even the best technical ideas are destined to remain undiscovered unless presented in a clear and compelling way that sparks innovation and drives adoption. For a decade, she’s traveled around the world to work with Top 100 corporations, institutions and universities, teaching the proven strategies she’s mastered through her consulting work and during her time as a faculty member at Northbrook State University. Dana is internationally known for her popular Lumen Stage talk entitled ‘Make It Matter to Me’ which has over 2 million views (and counting!). Teams that work with Dana get the practical skills and natural confidence they need to immediately shift their “information dump” style presentations into ones that are meaningful, engaging, and inspire people to take action. Dana provides on-site group workshops and coaching, conference sessions and keynotes, and 1:1 consultation.<span class="quote-mark quote-mark--close">”</span></p>
      <div class="meet">
        <p class="meet__name">Meet Dana</p>
        <p class="meet__tag">Science not communicated is science not done</p>
      </div>
    </div>
  </div>

  <footer class="band band--bio">
    <div class="contact">
      <div class="contact__row">
        <svg width="18" height="18" viewBox="0 0 18 18" fill="none" stroke="#fff" stroke-width="1.5"><circle cx="9" cy="9" r="7.5"/><ellipse cx="9" cy="9" rx="3.5" ry="7.5"/><path d="M1.5,9 H16.5"/></svg>
        www.CraftTalkStudio.example
      </div>
      <div class="contact__row">
        <svg width="18" height="18" viewBox="0 0 18 18" fill="none" stroke="#fff" stroke-width="1.5"><rect x="1.5" y="4" width="15" height="10" rx="1"/><path d="M1.5,4 L9,10 L16.5,4"/></svg>
        dana@crafttalkstudio.example
      </div>
    </div>
    <div class="band__rule"></div>
    <div>
      <p class="follow">Follow Us:</p>
      <div class="follow__icons"><span></span><span></span><span></span></div>
    </div>
  </footer>
</section>

</body>
</html>
```